Business Card Design Project

We need a business card designed for a new Luxury Custom Homebuilding company based in Arizona. We previous were called "Belcrest Estates" but want to start using "Belcrest Custom Homes" We want the message to communicate high end, luxury and cutting-edge. We like the blue, white and black color scheme.
Belcrest Custom Homes
Marcus T. Halloway
Chief Executive Officer
Office: 480-555-0142
Mobile: 480-555-0178
email: marc@belcrestcustom-example.com
web adress: www.BelcrestCustom-example.com
Updates
We have made a change to our website address and email address based on recieving feedback from a nmber of individuals. The feedback was web address and email address was to long. Therefore we have made a change. The new web adress and email adress are the following.
www.BelcrestCustom-example.com
marc@belcrestcustom-example.com
Also I decided against using in yellow. I like the colors blue,black, white and maybe gray.
Target Market(s)
Our target market is the wealthy individuals looking for a luxury high-end custom home.
Industry/Entity Type
Business
Look and feel

```html
<!DOCTYPE html>
<html lang="en">
<head>
<meta charset="utf-8">
<title>Belcrest Custom Homes – Business Card</title>
<link href="https://fonts.googleapis.com/css2?family=Jost:wght@400;500;600;700;800&display=swap" rel="stylesheet">
<style>
  :root {
    --ink: #050505;
    --sky: #5b9bd5;
    --paper: #ffffff;
    --slate: #5a5a5a;
    --stage: #a08068;
    --label: #111111;
  }
  * { margin: 0; padding: 0; box-sizing: border-box; }
  html, body { width: 1200px; height: 788px; overflow: hidden; }
  body {
    position: relative;
    background: var(--stage);
    font-family: "Jost", "Helvetica Neue", Arial, sans-serif;
    color: var(--paper);
  }
  .side-label {
    position: absolute;
    font-size: 21px;
    font-weight: 400;
    color: var(--label);
    text-align: center;
    width: 200px;
  }
  .side-label--front { left: 500px; top: 32px; }
  .side-label--back-one { left: 222px; top: 403px; }
  .side-label--back-two { left: 797px; top: 403px; }

  .card {
    position: absolute;
    width: 525px;
    height: 300px;
    border-radius: 22px;
    overflow: hidden;
  }
  .card--front { left: 338px; top: 83px; background: var(--ink); }
  .card--back-one { left: 54px; top: 445px; background: var(--sky); }
  .card--back-two { left: 622px; top: 445px; background: var(--ink); }

  .front-wave { position: absolute; left: 0; top: 0; width: 525px; height: 300px; }

  .wordmark {
    position: absolute;
    color: var(--paper);
    font-weight: 700;
    text-align: center;
    line-height: 1;
  }
  .wordmark__name { display: block; letter-spacing: -1px; }
  .wordmark__tag { display: block; text-transform: uppercase; letter-spacing: 1px; }

  .card--front .wordmark { left: 36px; top: 82px; width: 230px; }
  .card--front .wordmark__name { font-size: 56px; }
  .card--front .wordmark__tag { font-size: 20px; margin-top: 4px; }

  .card--back-one .wordmark,
  .card--back-two .wordmark { left: 0; top: 102px; width: 525px; }
  .card--back-one .wordmark__name,
  .card--back-two .wordmark__name { font-size: 82px; }
  .card--back-one .wordmark__tag,
  .card--back-two .wordmark__tag { font-size: 28px; margin-top: 6px; letter-spacing: 2px; }

  .contact {
    position: absolute;
    left: 302px;
    top: 56px;
  }
  .contact__name { font-size: 17px; font-weight: 600; line-height: 1.2; }
  .contact__title { font-size: 13.5px; font-weight: 400; margin-top: 2px; }
  .contact__list { list-style: none; margin-top: 10px; }
  .contact__item {
    display: flex;
    align-items: center;
    gap: 6px;
    font-size: 13px;
    line-height: 20px;
  }
  .contact__icon { width: 11px; height: 11px; flex: none; fill: var(--paper); }

  .address {
    position: absolute;
    left: 34px;
    top: 251px;
    font-size: 12px;
    line-height: 17px;
    color: var(--paper);
  }

  .back-url {
    position: absolute;
    left: 0;
    top: 257px;
    width: 525px;
    text-align: center;
    font-size: 17px;
    letter-spacing: 1.3px;
  }
</style>
</head>
<body>

  <div class="side-label side-label--front">Front</div>
  <div class="side-label side-label--back-one">Back - 1</div>
  <div class="side-label side-label--back-two">Back - 2</div>

  <section class="card card--front" aria-label="Card front">
    <svg class="front-wave" viewBox="0 0 525 300" aria-hidden="true">
      <path d="M0,210 C160,196 300,266 525,270 L525,300 L0,300 Z" fill="var(--sky)"/>
      <path d="M120,204 C270,206 390,246 525,226 L525,252 C400,268 270,236 120,204 Z" fill="var(--slate)"/>
      <path d="M50,205 C210,204 330,262 525,250 L525,266 C330,282 210,222 50,205 Z" fill="var(--paper)"/>
    </svg>

    <div class="wordmark">
      <span class="wordmark__name">Belcrest</span>
      <span class="wordmark__tag">Custom Homes</span>
    </div>

    <div class="contact">
      <div class="contact__name">Marcus T. Halloway</div>
      <div class="contact__title">Chief Executive Office</div>
      <ul class="contact__list">
        <li class="contact__item">
          <svg class="contact__icon" viewBox="0 0 12 12" aria-hidden="true"><path d="M1,4 C1,2 3,1 6,1 C9,1 11,2 11,4 L8.5,4.5 L8,3 L4,3 L3.5,4.5 Z M3,6 L9,6 L10.5,11 L1.5,11 Z"/></svg>
          480-555-0142
        </li>
        <li class="contact__item">
          <svg class="contact__icon" viewBox="0 0 12 12" aria-hidden="true"><path d="M3.5,0.5 H8.5 V11.5 H3.5 Z M4.5,2 V7 H7.5 V2 Z"/></svg>
          480-555-0178
        </li>
        <li class="contact__item">
          <svg class="contact__icon" viewBox="0 0 12 12" aria-hidden="true"><path d="M0.5,3 H11.5 V10 H0.5 Z M1.5,4 L6,7 L10.5,4 Z" fill-rule="evenodd"/></svg>
          marc@belcrestcustom-example.com
        </li>
        <li class="contact__item">
          <svg class="contact__icon" viewBox="0 0 12 12" aria-hidden="true"><circle cx="6" cy="6" r="5" fill="none" stroke="var(--paper)" stroke-width="1"/><ellipse cx="6" cy="6" rx="2.2" ry="5" fill="none" stroke="var(--paper)" stroke-width="1"/><path d="M1,6 H11" stroke="var(--paper)" stroke-width="1"/></svg>
          www.BelcrestCustom-example.com
        </li>
      </ul>
    </div>

    <address class="address" style="font-style:normal">
      2718 E. Ridgeview Lane<br>
      Suite 204, Mesa, AZ 85299
    </address>
  </section>

  <section class="card card--back-one" aria-label="Card back, blue version">
    <div class="wordmark">
      <span class="wordmark__name">Belcrest</span>
      <span class="wordmark__tag">Estates</span>
    </div>
    <div class="back-url">www.BelcrestCustom-example.com</div>
  </section>

  <section class="card card--back-two" aria-label="Card back, black version">
    <div class="wordmark">
      <span class="wordmark__name">Belcrest</span>
      <span class="wordmark__tag">Estates</span>
    </div>
    <div class="back-url">www.BelcrestCustom-example.com</div>
  </section>

</body>
</html>
```